Photoshop Design Project

Just looking to use some existing element in emails and printed flyers for a lunch menu promo.

I am attaching a menu in progress to reference only the front page design of a chalkboard, chalk fonts, tagline of :Break from the Status Quo for Lunch On The GO. Its on the front of the menu.

I just want to drop in a photo of each on three separate pieces with description.

THe design should not be a match to the front of the menu, just utilize its elements. the design is not a lead at all, these should remain familiar with the front of the menu, but please use the elements to your design preference.

Ok to submit one layout that we can repeat, or ok to submit three different versions

Must stick with the colors though, they are brand color combo, not exact by color code, but the oranges and the browns need to stay somewhere and in some capacity.
SO menu attached, check out the front cover for inspirations, to go in email sends embedded, and to print as a flyer.

There are also three images attached they are the to be dropped into each piece, with a desciption
Updates

Project Deadline Extended
Reason: seems to be too many questions and I wasnt getting anywhere.. To clarify...One Design Piece (one page), three separate items, same peice, however three total. one for each product photo supplied

I moved the deadline back as there were many questions. To clarify, one design piece to be reused for three different products (sandwiches in this case) Same piece, but one for each sandwich.

I posted a file called Artmarket that now has each photo partnered with its title and description

Target Market(s)

hungry people looking for lunch

Industry/Entity Type

Promo

Requirements
Must have
• Attached Menu front page elements, of chalkboard, chalk font existing front colors.

```html
<!DOCTYPE html>
<html lang="en">
<head>
<meta charset="utf-8">
<title>Lunch On The Go – Sandwich Promo Cards</title>
<link href="https://fonts.googleapis.com/css2?family=Cabin+Sketch:wght@400;700&family=Architects+Daughter&family=Great+Vibes&display=swap" rel="stylesheet">
<style>
  :root{
    --stage:#1d1d1e;
    --frame:#ffffff;
    --chalk-dark:#2f2f30;
    --chalk-mid:#3d3d3e;
    --chalk-ink:#f2f2ee;
    --brand-orange:#ee7d2e;
  }
  *{box-sizing:border-box;margin:0;padding:0}
  html,body{width:1200px;height:900px;overflow:hidden;background:var(--stage)}
  .stage{position:relative;width:1200px;height:900px;background:var(--stage)}

  .promo-card{position:absolute;background:var(--frame);box-shadow:0 4px 14px rgba(0,0,0,.55)}
  .promo-card--bbq{left:27px;top:25px;width:604px;height:340px;z-index:2}
  .promo-card--roast{left:573px;top:295px;width:593px;height:340px;z-index:1}
  .promo-card--steak{left:27px;top:533px;width:604px;height:340px;z-index:2}

  .food-photo{position:absolute;top:12px;left:13px;height:316px}
  .promo-card--bbq .food-photo,.promo-card--steak .food-photo{width:320px}
  .promo-card--roast .food-photo{left:17px;width:338px;top:12px;height:315px}

  .photo-bbq{background:linear-gradient(135deg,#d9b27a 0%,#6f3d1d 35%,#4f7a2c 55%,#c8452f 75%,#e4c18b 100%)}
  .photo-roast{background:linear-gradient(160deg,#e8c485 0%,#c98d3c 30%,#c7c59a 48%,#8a5a4e 62%,#d89a4a 80%,#f2e4c4 100%)}
  .photo-steak{background:linear-gradient(165deg,#e7c48d 0%,#d8a665 32%,#9e4d3e 55%,#c4786a 72%,#5a6e35 100%)}

  .accent-bars{position:absolute;top:12px;left:13px;height:316px;width:42px}
  .accent-bars span{position:absolute;top:0;bottom:0;background:var(--brand-orange)}
  .accent-bars .bar-wide{left:0;width:16px}
  .accent-bars .bar-gap{left:16px;width:12px;background:rgba(255,255,255,.75)}
  .accent-bars .bar-thin{left:28px;width:13px}
  .promo-card--roast .accent-bars{left:17px}

  .chalk-panel{position:absolute;top:12px;height:316px;color:var(--chalk-ink);overflow:hidden;
    background:radial-gradient(ellipse at 40% 35%,var(--chalk-mid) 0%,var(--chalk-dark) 75%)}
  .promo-card--bbq .chalk-panel,.promo-card--steak .chalk-panel{left:333px;width:260px}
  .promo-card--roast .chalk-panel{left:355px;width:226px;height:315px}

  .chalk-rule{position:absolute;inset:0;width:100%;height:100%}
  .chalk-rule path{fill:none;stroke:var(--brand-orange);stroke-width:3;stroke-linecap:round;stroke-linejoin:round}

  .sandwich-title{position:absolute;font-family:"Cabin Sketch",cursive;font-weight:400;
    text-transform:uppercase;font-size:25px;line-height:30px;letter-spacing:1px;text-align:center;white-space:nowrap}
  .sandwich-title .initial{font-family:"Great Vibes",cursive;font-size:52px;line-height:20px;
    text-transform:none;vertical-align:-6px;margin-right:2px}

  .sandwich-desc{position:absolute;font-family:"Architects Daughter",cursive;text-transform:uppercase;
    font-size:12.5px;line-height:16.5px;letter-spacing:1px;text-align:right;white-space:nowrap}

  .promo-card--bbq .sandwich-title{left:14px;top:22px;width:236px;text-align:left}
  .promo-card--bbq .sandwich-desc{right:14px;top:160px}
  .promo-card--roast .sandwich-title{left:34px;top:12px;width:190px;line-height:31px}
  .promo-card--roast .sandwich-desc{right:12px;top:228px}
  .promo-card--steak .sandwich-title{left:14px;top:18px;width:240px;font-size:22px;line-height:27px}
  .promo-card--steak .sandwich-desc{right:14px;top:228px}
</style>
</head>
<body>
<main class="stage">

  <article class="promo-card promo-card--bbq">
    <div class="food-photo photo-bbq" role="img" aria-label="Photo of grilled BBQ chicken sandwich on focaccia with micro greens and red pepper"></div>
    <div class="accent-bars"><span class="bar-wide"></span><span class="bar-gap"></span><span class="bar-thin"></span></div>
    <section class="chalk-panel">
      <svg class="chalk-rule" viewBox="0 0 260 316" aria-hidden="true">
        <path d="M40 146 C30 150 24 142 30 136 C36 130 44 138 40 146 L248 143 M40 146 L44 306"/>
      </svg>
      <h2 class="sandwich-title"><span class="initial">B</span>istro BBQ<br>&nbsp;&nbsp;Chicken<br>&nbsp;&nbsp;Sandwich</h2>
      <p class="sandwich-desc">Perfectly grilled<br>BBQ chicken<br>breast, dill yogurt<br>dressing, garlic<br>spread, micro greens,<br>radish, &amp; red<br>bell pepper<br>on fresh<br>focaccia bread</p>
    </section>
  </article>

  <article class="promo-card promo-card--roast">
    <div class="food-photo photo-roast" role="img" aria-label="Photo of spicy roast beef sandwich on ciabatta with sprouts and basil"></div>
    <div class="accent-bars"><span class="bar-wide"></span><span class="bar-gap"></span><span class="bar-thin"></span></div>
    <section class="chalk-panel">
      <svg class="chalk-rule" viewBox="0 0 226 315" aria-hidden="true">
        <path d="M60 213 C50 217 44 209 50 203 C56 197 64 205 60 213 L212 214 M60 213 L62 306"/>
      </svg>
      <h2 class="sandwich-title"><span class="initial">S</span>picy<br>Roast Beef<br>Sandwich<br>with Danish<br>Smelly<br>Cheese</h2>
      <p class="sandwich-desc">Sprouts, fresh<br>basil, onions &amp;<br>chili sauce<br>on a fresh<br>ciabatta roll</p>
    </section>
  </article>

  <article class="promo-card promo-card--steak">
    <div class="food-photo photo-steak" role="img" aria-label="Photo of sliced steak sandwich on ciabatta with watercress"></div>
    <div class="accent-bars"><span class="bar-wide"></span><span class="bar-gap"></span><span class="bar-thin"></span></div>
    <section class="chalk-panel">
      <svg class="chalk-rule" viewBox="0 0 260 316" aria-hidden="true">
        <path d="M62 205 C52 209 46 201 52 195 C58 189 66 197 62 205 L246 206 M62 205 L64 306"/>
      </svg>
      <h2 class="sandwich-title"><span class="initial">S</span>teak Sandwich<br>with Blue Cheese,<br>Roasted Garlic<br>Mayonnaise &amp;<br>Balsamic Vinegar<br>Reduction</h2>
      <p class="sandwich-desc">Topped with<br>Roquefort cheese<br>&amp; watercress<br>on fresh<br>ciabatta bread</p>
    </section>
  </article>

</main>
</body>
</html>
```